Talrexa Website Design

Talrexa Solutions. http://talrexasolutions.example is looking to redesign our current website with a modern feel and added functionality.

The winning design will be coded in HTML 5 and be responsive built for mobile. You can use bootstrap, jquery.

Wordpress or wix will not be accepted.

Page 1
http://talrexasolutions.example/

Page 2
http://talrexasolutions.example/who_we_are.php

Page 3
http://talrexasolutions.example/solutions_offered.php

Page 4
http://talrexasolutions.example/faq.php

Here are some pages from our competitors. Please see notes of our likes and dislikes of each page.

https://www.quorvanhealthcare.example/

Likes: Ability to explore opportunities / “Neighbourhood Ties” Highlighting involvement in the community.

Dislike: Layout not very interactive. Feels clunky

https://www.pelnarhealth.example/

Likes: Visually appealing. Using nice images.

Dislike: Not very intuitive. You need to read a bit to figure out what they do and what they’re about.. Not overly interactive either.

https://brevonsolutions.example/

Likes: Clean, Using a puppy as part of marketing, highlights Stability and Quality

Dislikes: All services offered are further down and requires you click and drill down to get info

https://www.tolmiqode.example/

Likes: Has video about Improving Coding Accuracy which is important to clients. Their “Our Solutions” Section is clear and not too wordy. Once you click on Learn More it provides good info.

Dislikes: Not as visually appealing. No wow factor. Seems a bit basic.

https://verdanhcs.example/

Likes: Section that allows clients to request facility analysis. Has easy to find menu dropdowns at the top of page.

Dislikes: Boring site. Nothing special at all.

https://kestrow.example/

Likes: I actually like this site overall

Dislikes: It is a little busy, but other than that it’s pretty nice.

https://zuvaro.example

Likes: although their choice of doodle graphics is overly busy, I like that it’s different from every other vendor. To me, it stands out. I also like how when you scroll, it pops up a new highlight and keeps the watermark in the background.

Dislikes: Choice of font is a lil hard to read and not easy on the eyes. I believe the bold and color of the font make it appear too busy.

https://falkwoodgroup.example/

Likes: Probably my favorite. Very professional and interactive. I like how it scrolls through images at the top with links to allow you to dive in further. I also like the interactive photo blocks towards the bottom and how they use photos from past speaking events that give them credibility and highlight Dr Falkwood speaking.

Dislikes: Nothing specific

Do to the ongoing Corona Virus here in Florida we have been dealing with that. Most will be working from home this week and plan to focus on finalizing this project. Thanks

Please extend this. With the current COVID19 stuff this is kind of been put on the back burner.

```html
<!DOCTYPE html>
<html lang="en">
<head>
<meta charset="utf-8">
<title>Who We Are – Talrexa Solutions</title>
<link href="https://fonts.googleapis.com/css2?family=Poppins:wght@400;500;600;700;800&display=swap" rel="stylesheet">
<style>
:root{
  --indigo:#3f49a1;
  --indigo-dark:#36418f;
  --green:#8fd68a;
  --ink:#222;
  --muted:#555;
  --soft:#f0f1f3;
  --white:#fff;
}
*{box-sizing:border-box;margin:0;padding:0}
html,body{width:1200px;height:2396px;overflow:hidden;background:var(--white)}
body{position:relative;font-family:"Poppins",sans-serif;color:var(--ink)}
.abs{position:absolute}
a{color:inherit;text-decoration:none}

/* header */
.site-header{position:absolute;left:0;top:0;width:1200px;height:110px;background:var(--white)}
.brand{left:86px;top:28px;font-size:30px;font-weight:600;color:var(--green);letter-spacing:1px;line-height:1}
.brand small{display:block;font-size:13px;letter-spacing:9px;margin-top:4px}
.topbar{left:603px;top:0;width:411px;height:39px;border-bottom:1px solid #e3e3e3;font-size:13px;color:#444}
.topbar .social{position:absolute;top:12px;display:flex;gap:30px;left:0}
.topbar .contact{position:absolute;right:34px;top:12px;display:flex;align-items:center;gap:6px}
.main-nav{left:429px;top:65px;display:flex;gap:30px;font-size:13px;font-weight:500;color:#222}
.header-cta{left:1016px;top:0;width:184px;height:110px;background:var(--green)}
.header-cta a{position:absolute;left:27px;top:33px;width:129px;height:43px;border:2px solid var(--white);color:var(--white);font-size:14px;font-weight:600;display:flex;align-items:center;justify-content:center}

/* hero */
.hero{left:0;top:110px;width:1200px;height:368px;background:linear-gradient(90deg,#8a8a8a 0%,#b9b7b4 35%,#cfcac4 60%,#d8d8da 100%)}
.hero-title{left:93px;top:245px;font-size:50px;font-weight:800;color:var(--white);letter-spacing:1px}
.breadcrumb{left:92px;top:313px;display:flex;align-items:center;gap:16px;font-size:14px;color:var(--white);font-weight:500}
.breadcrumb .current{color:var(--green)}

/* mission */
.mission-photo{left:86px;top:572px;width:332px;height:396px;background:linear-gradient(180deg,#e9ecf2 0%,#d9dee8 60%,#c8cfdc 100%);border-radius:40% 40% 6px 6px}
.mission-kicker{left:474px;top:624px;font-size:36px;font-weight:600;color:var(--indigo);line-height:1}
.mission-title{left:470px;top:655px;font-size:88px;font-weight:700;color:var(--indigo);line-height:1;letter-spacing:1px}
.mission-rule{left:476px;top:771px;width:85px;height:2px;background:var(--green)}
.mission-text{left:578px;top:759px;width:548px;font-size:15px;line-height:20px;color:var(--muted)}

/* values */
.values{left:0;top:968px;width:1200px;height:415px;background:var(--soft)}
.section-title{left:0;width:1200px;text-align:center;font-weight:600;color:var(--indigo);line-height:1}
.title-rule{width:58px;height:3px;background:var(--green)}
.value-line{left:90px;top:1255px;width:1020px;border-top:1px dashed #b5b5b5}
.value{position:absolute;top:1133px;width:220px;margin-left:-110px;text-align:center}
.value svg{display:block;margin:0 auto;height:62px}
.value h3{margin-top:25px;font-size:17px;font-weight:600;color:#222;letter-spacing:.5px;line-height:25px}
.value .dot{display:block;width:12px;height:12px;border:2px solid #b5b5b5;border-radius:50%;background:var(--soft);margin:4px auto 0}
.value p{margin-top:20px;font-size:14px;line-height:20px;color:var(--muted)}

/* opportunities */
.apply-note{left:0;top:1533px;width:1200px;text-align:center;font-size:14px;font-weight:600;letter-spacing:.5px}
.apply-btn{left:535px;top:1571px;width:131px;height:43px;background:var(--green);color:var(--white);font-size:14px;font-weight:600;display:flex;align-items:center;justify-content:center}
.team-photo{left:0;top:1618px;width:1200px;height:360px;background:radial-gradient(ellipse at 50% 70%,#5c6a8f 0%,#8a90a8 35%,#c9ccd6 65%,rgba(255,255,255,0) 85%)}

/* footer */
.site-footer{left:0;top:1978px;width:1200px;height:364px;background:var(--indigo);color:var(--white)}
.footer-brand{left:88px;top:2128px;font-size:34px;font-weight:600;color:var(--white);line-height:1;letter-spacing:1px}
.footer-brand small{display:block;font-size:15px;letter-spacing:12px;margin-top:6px}
.footer-heading{font-size:14px;font-weight:600;letter-spacing:.4px;color:var(--white)}
.footer-links{left:374px;top:2094px;list-style:none;font-size:13px;line-height:31px;color:var(--white)}
.contact-item{position:absolute;left:579px;font-size:13px;line-height:22px;padding-left:23px;color:var(--white)}
.contact-item svg{position:absolute;left:0;top:4px}
.newsletter-text{left:852px;top:2096px;width:230px;font-size:13px;line-height:19px;color:var(--white)}
.newsletter-form{left:852px;top:2149px;width:257px;height:44px;background:var(--white);display:flex}
.newsletter-form span{flex:1;display:flex;align-items:center;gap:8px;padding-left:15px;font-size:13px;color:#555}
.newsletter-form button{width:39px;border:0;background:var(--green);display:flex;align-items:center;justify-content:center}
.round{position:absolute;width:34px;height:34px;border-radius:50%;background:rgba(255,255,255,.12);display:flex;align-items:center;justify-content:center}
.copyright{left:0;top:2342px;width:1200px;height:54px;background:var(--indigo-dark);color:var(--white);font-size:13px;display:flex;align-items:center;justify-content:center}
.to-top{left:1136px;top:2324px;width:36px;height:36px;border-radius:50%;background:var(--white);display:flex;align-items:center;justify-content:center}
</style>
</head>
<body>

<header class="site-header">
  <div class="abs brand">TALREXA<small>SOLUTIONS</small></div>
  <div class="abs topbar">
    <div class="social">
      <svg width="10" height="10"><rect x="1" y="1" width="8" height="8" fill="none" stroke="#666" stroke-width="1.3"/></svg>
      <svg width="10" height="10"><circle cx="5" cy="5" r="4" fill="none" stroke="#666" stroke-width="1.3"/></svg>
    </div>
    <div class="contact">
      <svg width="12" height="12" viewBox="0 0 24 24"><path d="M6.6 10.8a15 15 0 0 0 6.6 6.6l2.2-2.2a1 1 0 0 1 1-.25 11 11 0 0 0 3.6.6 1 1 0 0 1 1 1V20a1 1 0 0 1-1 1A17 17 0 0 1 3 4a1 1 0 0 1 1-1h3.5a1 1 0 0 1 1 1 11 11 0 0 0 .6 3.6 1 1 0 0 1-.25 1z" fill="#666"/></svg>
      <span>CONTACT US: <b style="font-weight:500">(555) 014-2290</b></span>
    </div>
  </div>
  <nav class="abs main-nav">
    <a href="#">HOME</a><a href="#">JOB SEARCH</a><a href="#">APPLY NOW</a><a href="#">ABOUT TALREXA</a><a href="#">SOLUTIONS</a><a href="#">LOGIN</a>
  </nav>
  <div class="abs header-cta"><a href="#">CONTACT US</a></div>
</header>

<section class="abs hero" role="img" aria-label="Photo of two smiling women, one a doctor in a white coat with a stethoscope"></section>
<h1 class="abs hero-title">WHO WE ARE</h1>
<div class="abs breadcrumb">
  <span style="display:flex;align-items:center;gap:6px"><svg width="18" height="16" viewBox="0 0 24 22"><path d="M12 1 1 11h3v10h6v-6h4v6h6V11h3z" fill="#fff"/></svg>HOME</span>
  <span>|</span>
  <span class="current">WHO WE ARE</span>
</div>

<div class="abs mission-photo" role="img" aria-label="Photo of a senior doctor in a white coat with arms crossed"></div>
<h2 class="abs mission-kicker">MISSION</h2>
<h2 class="abs mission-title">STATEMENT</h2>
<div class="abs mission-rule"></div>
<p class="abs mission-text">To transform the idea of healthcare services by focusing on the highest standards of quality for our clients, while maintaining world-class customer care for our consultants.</p>

<section class="abs values"></section>
<h2 class="abs section-title" style="top:1052px;font-size:36px">CORE VALUES</h2>
<div class="abs title-rule" style="left:571px;top:1099px"></div>
<div class="abs value-line"></div>

<div class="value" style="left:176px">
  <svg viewBox="0 0 70 64" width="70"><circle cx="19" cy="12" r="9" fill="none" stroke="#3f49a1" stroke-width="2.5"/><path d="M3 40a16 14 0 0 1 32 0z" fill="#8fd68a" stroke="#3f49a1" stroke-width="2.5"/><circle cx="48" cy="46" r="14" fill="none" stroke="#3f49a1" stroke-width="2.5" stroke-dasharray="5 3"/><circle cx="48" cy="46" r="6" fill="none" stroke="#3f49a1" stroke-width="2.5"/></svg>
  <h3>ADAPT</h3><span class="dot"></span>
  <p>Continuous improvement<br>and education.</p>
</div>
<div class="value" style="left:397px">
  <svg viewBox="0 0 50 64" width="50"><path d="M25 3 4 11v20c0 15 10 25 21 30 11-5 21-15 21-30V11z" fill="none" stroke="#3f49a1" stroke-width="2.5"/><path d="M25 10 10 16v15c0 10 7 18 15 22 8-4 15-12 15-22V16z" fill="#8fd68a" opacity=".5"/><path d="M15 32l7 7 13-14" fill="none" stroke="#3f49a1" stroke-width="3"/></svg>
  <h3>INTEGRITY</h3><span class="dot"></span>
  <p>Do what is right.</p>
</div>
<div class="value" style="left:600px">
  <svg viewBox="0 0 60 64" width="60"><path d="M30 40C10 26 8 16 14 9s14-3 16 3c2-6 10-10 16-3s4 17-16 31z" fill="#8fd68a" stroke="#3f49a1" stroke-width="2"/><path d="M3 46h10v14H3zM13 48h16l5 3h-12M13 58h22l20-12-4-3-16 7" fill="none" stroke="#3f49a1" stroke-width="2.5"/></svg>
  <h3>PASSION</h3><span class="dot"></span>
  <p>Strive for Excellence.</p>
</div>
<div class="value" style="left:824px">
  <svg viewBox="0 0 76 64" width="76"><path d="M4 22 16 8l9 8-12 14zM72 22 60 8l-9 8 12 14z" fill="none" stroke="#3f49a1" stroke-width="2.5"/><path d="M25 16h14l-8 8 5 4 10-8 12 12" fill="#8fd68a" stroke="#3f49a1" stroke-width="2.5"/><path d="M13 30l20 22c3 3 7 0 5-3l3 3c3 2 6-1 4-4l2 2c3 2 6-1 4-4l-9-10" fill="none" stroke="#3f49a1" stroke-width="2.5"/></svg>
  <h3>COMMITMENT</h3><span class="dot"></span>
  <p>Dedication to clients,<br>employees &amp; community.</p>
</div>
<div class="value" style="left:1057px">
  <svg viewBox="0 0 70 64" width="70"><path d="M35 6v52M22 58h26M12 14h46" fill="none" stroke="#3f49a1" stroke-width="2.5"/><circle cx="35" cy="6" r="3" fill="#3f49a1"/><path d="M12 14 4 32h16zM58 14l-8 18h16z" fill="none" stroke="#3f49a1" stroke-width="2"/><path d="M3 32a9 7 0 0 0 18 0zM49 32a9 7 0 0 0 18 0z" fill="#8fd68a" stroke="#3f49a1" stroke-width="2"/><path d="M30 50h10l3 8H27z" fill="#8fd68a" stroke="#3f49a1" stroke-width="2"/></svg>
  <h3>BALANCE</h3><span class="dot"></span>
  <p>Evaluate what is<br>important.</p>
</div>

<h2 class="abs section-title" style="top:1469px;font-size:36px">OPPORTUNITIES AVAILABLE IN MIAMI, FL</h2>
<div class="abs title-rule" style="left:571px;top:1513px"></div>
<p class="abs apply-note">CLICK BELOW TO APPLY.</p>
<div class="abs team-photo" role="img" aria-label="Photo of six young people sitting together holding tablets and clipboards, looking up"></div>
<a class="abs apply-btn" href="#">APPLY NOW</a>

<footer class="abs site-footer"></footer>
<div class="abs footer-brand">TALREXA<small>SOLUTIONS</small></div>

<h4 class="abs footer-heading" style="left:374px;top:2053px">QUICK LINKS</h4>
<ul class="abs footer-links">
  <li>Home</li><li>Job Search</li><li>Apply Now</li><li>About Talrexa Solutions</li><li>Login</li><li>Join Commission</li>
</ul>

<h4 class="abs footer-heading" style="left:579px;top:2053px">CONTACT US</h4>
<div class="contact-item" style="top:2094px">
  <svg width="14" height="11" viewBox="0 0 14 11"><rect width="14" height="11" rx="1" fill="#8fd68a"/><path d="M0 1l7 5 7-5" stroke="#3f49a1" fill="none"/></svg>
  Email:<br>jobs@talrexasolutions.example
</div>
<div class="contact-item" style="top:2156px">
  <svg width="14" height="14" viewBox="0 0 24 24"><path d="M6.6 10.8a15 15 0 0 0 6.6 6.6l2.2-2.2a1 1 0 0 1 1-.25 11 11 0 0 0 3.6.6 1 1 0 0 1 1 1V20a1 1 0 0 1-1 1A17 17 0 0 1 3 4a1 1 0 0 1 1-1h3.5a1 1 0 0 1 1 1 11 11 0 0 0 .6 3.6 1 1 0 0 1-.25 1z" fill="#8fd68a"/></svg>
  Telephone:<br>(555) 014-2290
</div>
<div class="contact-item" style="top:2218px">
  <svg width="12" height="16" viewBox="0 0 12 16"><path d="M6 0a6 6 0 0 0-6 6c0 4 6 10 6 10s6-6 6-10a6 6 0 0 0-6-6z" fill="#8fd68a"/><circle cx="6" cy="6" r="2" fill="#3f49a1"/></svg>
  Location:<br>2740 Harbor Crest Ave Suite 410<br>Larkfield Bay, LB 00410
</div>

<h4 class="abs footer-heading" style="left:852px;top:2055px">NEWSLETTER</h4>
<p class="abs newsletter-text">Subscribe to our email address to get the latest news.</p>
<div class="abs newsletter-form">
  <span><svg width="13" height="10"><rect width="13" height="10" rx="1" fill="#ccc"/><path d="M0 1l6.5 4.5L13 1" stroke="#fff" fill="none"/></svg>Enter Your Email...</span>
  <button type="button" aria-label="Subscribe"><svg width="18" height="16" viewBox="0 0 18 16"><path d="M0 7 18 0l-4 16-5-5-3 4V10l9-8-11 7z" fill="#fff"/></svg></button>
</div>
<span class="round" style="left:853px;top:2214px"><svg width="10" height="10"><rect x="1" y="1" width="8" height="8" fill="none" stroke="#fff" stroke-width="1.3"/></svg></span>
<span class="round" style="left:895px;top:2214px"><svg width="10" height="10"><circle cx="5" cy="5" r="4" fill="none" stroke="#fff" stroke-width="1.3"/></svg></span>

<div class="abs copyright">2020 © Talrexa Solutions, Inc</div>
<a class="abs to-top" href="#" aria-label="Back to top"><svg width="10" height="14" viewBox="0 0 10 14"><path d="M5 13V1M1 5l4-4 4 4" stroke="#333" fill="none" stroke-width="1.2"/></svg></a>

</body>
</html>
```